Tri-fold Brochure Design for Law Firm

I need a tri-fold brochure to give to prospective clients.
I have attached a Photoshop design file of a tri-fold brochure. The content (copy) is good, however, he brochure itself looks very amateurish.
I want a professional, sophisticated looking brochure.
The law firm specializes in commercial debt collection.
The law firm is located in New York City.
Our target market is business owners, doctors, lawyers, collection agencies and accountants.
Visit my website which is being designed at www.dornvek.com. I like the font used for the name of my company and the rich blue color used.

Target Market(s)

Business Owners, Doctors, Law Firms and Accountants

Industry/Entity Type

Law Firm

Font styles to use
Serif

Requirements
Must have
• Professional quality graphic work. Attention to details.
• PHOTOGRAPHS ONLY, NO CLIP-ART.
• DARK COLORS - NAVY BLUE, HUNTER GREEN, BLACK, GRAY & WHITE
Nice to have
• I want it to look smart, modern and sophisticated.
• Visit my website which is being designed at www.dornvek.com. I like the font used for the name of my company and the rich blue color used.
Should not have
• Bad artwork
• CLIP ART

```html
<!DOCTYPE html>
<html lang="en">
<head>
<meta charset="utf-8">
<title>Corwin Halden &amp; Company – Tri-fold Brochure</title>
<link href="https://fonts.googleapis.com/css2?family=Roboto+Condensed:wght@400;700&family=Roboto:wght@400;700&display=swap" rel="stylesheet">
<style>
  :root{
    --navy:#2a3a8c;
    --navy-deep:#1f2a6b;
    --sky:#1ea3dd;
    --heading-blue:#2b3f97;
    --ink:#2e2e2e;
    --white:#ffffff;
  }
  html,body{margin:0;padding:0;overflow:hidden;background:#fff;}
  .brochure{position:relative;width:1200px;height:927px;overflow:hidden;background:var(--white);
    font-family:"Roboto Condensed","Roboto",sans-serif;color:var(--ink);}
  .artwork{position:absolute;inset:0;}
  .section{position:absolute;}
  .section h2{margin:0 0 10px;font-family:"Roboto Condensed",sans-serif;font-weight:700;
    font-size:21px;line-height:1.1;color:var(--heading-blue);letter-spacing:.1px;}
  .section h2.small{font-size:19px;}
  .section p{margin:0 0 9px;font-size:13.8px;line-height:17.3px;text-align:justify;text-indent:22px;}
  .on-navy h2,.on-navy p,.on-navy li{color:var(--white);}
  .fee-list{list-style:none;margin:14px 0 0;padding:0 0 0 38px;}
  .fee-list li{position:relative;font-weight:700;font-size:17.5px;line-height:28.4px;padding-left:22px;}
  .fee-list li::before{content:"";position:absolute;left:0;top:9px;width:8px;height:8px;border:1.5px solid var(--white);border-radius:50%;}
  .fee-list li::after{content:"";position:absolute;left:3.5px;top:12.5px;width:4px;height:4px;background:var(--white);border-radius:50%;}
  .act{text-decoration:underline;font-style:italic;}
  .firm{font-weight:700;}
</style>
</head>
<body>
<div class="brochure">
  <svg class="artwork" width="1200" height="927" viewBox="0 0 1200 927" xmlns="http://www.w3.org/2000/svg">
    <defs>
      <linearGradient id="skyline" x1="0" y1="0" x2="0" y2="1">
        <stop offset="0" stop-color="#e9a06a"/>
        <stop offset=".35" stop-color="#b89a8a"/>
        <stop offset=".7" stop-color="#5e646e"/>
        <stop offset="1" stop-color="#3b3f48"/>
      </linearGradient>
      <linearGradient id="tower" x1="0" y1="0" x2="1" y2="1">
        <stop offset="0" stop-color="#2f3f93"/>
        <stop offset="1" stop-color="#24306f"/>
      </linearGradient>
      <clipPath id="above-wave">
        <path d="M0,0 H1200 V370 C900,400 750,420 600,360 C450,300 200,290 0,340 Z"/>
      </clipPath>
      <clipPath id="below-wave">
        <path d="M0,372 C200,350 400,380 600,420 C800,470 1000,520 1200,520 L1200,927 L0,927 Z"/>
      </clipPath>
    </defs>

    <rect x="403" y="0" width="403" height="868" fill="url(#tower)" role="img" aria-label="Photo of a glass office tower seen from below, tinted navy"/>
    <rect x="0" y="0" width="403" height="420" fill="url(#skyline)" clip-path="url(#above-wave)" role="img" aria-label="Photo of the New York City skyline at sunset"/>
    <rect x="806" y="0" width="394" height="460" fill="var(--white)" clip-path="url(#above-wave)"/>

    <path d="M0,340 C200,290 450,300 600,360 S900,400 1200,370 L1200,520 C1000,520 800,470 600,420 C400,380 200,350 0,372 Z" fill="var(--navy)"/>
    <path d="M0,348 C200,300 450,310 600,368 S900,408 1200,378 L1200,470 C1000,480 800,440 600,398 C400,358 200,342 0,360 Z" fill="var(--sky)"/>

    <rect x="0" y="340" width="403" height="540" fill="var(--white)" clip-path="url(#below-wave)"/>
    <rect x="806" y="400" width="394" height="480" fill="var(--white)" clip-path="url(#below-wave)"/>

    <circle cx="506" cy="410" r="82" fill="var(--sky)"/>
    <circle cx="506" cy="410" r="75" fill="var(--white)"/>
    <rect x="466" y="370" width="80" height="26" rx="6" fill="#e8702a" role="img" aria-label="Compliance certification badge"/>
    <rect x="472" y="420" width="68" height="22" rx="6" fill="#5a6aa8" role="img" aria-label="Health privacy compliance badge"/>

    <rect x="0" y="868" width="1200" height="5" fill="var(--sky)"/>
    <rect x="0" y="875" width="1200" height="52" fill="var(--navy-deep)"/>
  </svg>

  <section class="section" style="left:28px;top:364px;width:348px;">
    <h2>WHO WE ARE</h2>
    <p><span class="firm">Corwin Halden &amp; Company, PLLC</span> is a New York based law firm devoted to the collection of accounts receivable and business debts.</p>
  </section>

  <section class="section" style="left:30px;top:459px;width:342px;">
    <h2>WHAT WE DO</h2>
    <p>Within 24 to 72 hours of receiving a claim, we will verify the debt, investigate the Debtor, skiptrace all known stakeholders and file a lawsuit with the intent of collecting the full amount due in the shortest time possible.</p>
    <p>We will use all legal means necessary to locate, identify, seize, or otherwise garnish a Debtor’s assets and income, while always having an attorney available to speak directly with the Debtor to achieve an amicable resolution as quickly as possible.</p>
  </section>

  <section class="section" style="left:28px;top:686px;width:345px;">
    <h2>OUR MISSION</h2>
    <p>Our mission is to protect our clients’ bottom line, while preserving their reputation.</p>
    <p>We recognize and appreciate that your Debtor was once a trusted customer and may be a source of future revenue.</p>
    <p>We treat all Debtors with respect, while agressively seeking the payment of all monies owed.</p>
  </section>

  <section class="section on-navy" style="left:432px;top:34px;width:342px;">
    <h2>FLEXIBLE FEE STRUCTURE</h2>
    <p>We recognize that each claim is unique, therefore, to better serve our clients we offer a variety of fee structures that meet the needs of our clients, including:</p>
    <ul class="fee-list">
      <li>Contingency Fee</li>
      <li>Flat Fee</li>
      <li>Hourly Fee</li>
      <li>Monthly or Annual Retainer</li>
      <li>Any combination of the above</li>
    </ul>
  </section>

  <section class="section on-navy" style="left:432px;top:513px;width:342px;">
    <h2>HANDLING MEDICAL RECEIVABLES</h2>
    <p>Medical receivables require a soft touch.</p>
    <p>Doctors and Healthcare Organizations often write-off tens of thousands of dollars in unpaid deductibles and co-insurance payments which are rightfully due them out of fear that pursuing these debts will alienate and upset patients.</p>
    <p>We offer non-legal, HIPPA compliant collection methods which can effectively and consistently turn these otherwise uncollected and ignored assets into real cash.</p>
    <p>Using a combination of letters and phone calls, our staff contacts patients in a non-threatening and friendly manner to arrange for payments, as small as $15 per month, encouraging them to pay all monies owed.</p>
  </section>

  <section class="section" style="left:834px;top:34px;width:333px;">
    <h2>CREDIT ADVISORY SERVICES</h2>
    <p>How well do you really know your customers?</p>
    <p>As an added service, we offer all of our clients a simple, customized credit application which can be used in the ordinary course of business.</p>
    <p>Working closely alongside our client's sales staff, we discretely review and verify their customer's information and investigate all known stakeholders to determine creditworthiness.</p>
    <p>Based on our findings, we make specific and meaningful recommendations, regarding the amount and terms credit should be offered to a customer. Once credit decision is made, we can provide the client with a credit agreement to be signed by the customer, detailing his obligations. Using such agreements minimizes risk, while enhancing our client's professional stature with their customers.</p>
  </section>

  <section class="section" style="left:834px;top:521px;width:336px;">
    <h2>KEEPING YOU IN COMPLIANCE</h2>
    <p>As your collection attorney and advisor, we will assure that your collection practices are in full compliance with all applicable Federal and State laws, including <span class="act">The Fair Debt Collection Practices Act</span> (FDCPA) and <span class="act">The Health Insurance Portability and Accountability Act</span> (HIPPA).</p>
  </section>

  <section class="section" style="left:834px;top:665px;width:334px;">
    <h2>STATE-OF-THE-ART TECHNOLOGY</h2>
    <p>Our firm prides itself on utilizing the state-of-the-art technology in law office management, telephony, cyber security, document production, and cloud storage.</p>
    <p>Our clients can be assured that their critical business data is stored in a safe, secure, and confidential environment, while allowing us to seamlessly handle a large and ever growing book of business in a timely manner.</p>
  </section>
</div>
</body>
</html>
```